Anzeigengestaltung für Heilpraktikerin für Psychotherapie
Hallo lorvik, ich bin sehr zufrieden mit dem Design. Danke LG Helga Brandner
Zielgruppe
Heilpraktikerin für Psychotherapie, Atem- und Körpertherapeutin, Einzelthearpie, Gruppentherapie, Menschen in Lebenskrisen; Menschen, die ihr Leben verändern wollen, Menschen suchen mehr Selbsterfahrung, vorwiegend Frauen, Atersgruppe 20 aufwärts, Menschen mit psychischen Problemen
Entspannung, Berühren, Massieren, Halten, Gespräch, Bewegen, Begleitung Während der Schwangerschaft, Geburt und danach, Trauerbegleitung
Aufgabenstellung
Name und Berufsbezeichnung sind mir wichtig
Praxiseröffnung, Termine nach Vereinbarung
aktuelles Angebot: Fantasiereise- Entspannung von Alltagsstress
sonstiges Angebot: Einzeltherapie/Gruppentherapie,

```html
<!DOCTYPE html>
<html lang="de">
<head>
<meta charset="utf-8">
<title>Praxiseröffnung – Helga Brandner</title>
<link rel="stylesheet" href="https://fonts.googleapis.com/css2?family=Crimson+Pro:wght@400;600;700&display=swap">
<style>
  :root {
    --plum: #6f2a58;
    --plum-text: #6a2654;
    --sky-top: #ddd1e8;
    --sky-mid: #b9a5d2;
    --sky-low: #9479b8;
    --shade: #4a3862;
    --meadow: #2f2440;
    --pink: #e4037f;
    --white: #ffffff;
  }
  * { box-sizing: border-box; margin: 0; padding: 0; }
  html, body { width: 800px; height: 1200px; overflow: hidden; background: #ffffff; }
  .ad {
    position: relative;
    width: 800px;
    height: 1200px;
    overflow: hidden;
    font-family: "Crimson Pro", Georgia, serif;
  }
  .ad__sky {
    position: absolute;
    inset: 0;
    background: linear-gradient(180deg, var(--sky-top) 0%, var(--sky-mid) 50%, var(--sky-low) 100%);
  }
  .ad__photo {
    position: absolute;
    left: 0;
    top: 600px;
    width: 800px;
    height: 600px;
    background:
      linear-gradient(180deg, transparent 0%, transparent 78%, var(--meadow) 100%),
      radial-gradient(ellipse 240px 420px at 560px 420px, rgba(74, 56, 98, 0.75) 0%, rgba(74, 56, 98, 0.35) 55%, transparent 100%),
      linear-gradient(180deg, transparent 0%, rgba(120, 96, 160, 0.45) 100%);
  }
  .topbar {
    position: absolute;
    top: 0; left: 0;
    width: 800px;
    height: 68px;
    background: var(--plum);
    color: var(--white);
    font-size: 28px;
    display: flex;
    align-items: center;
    justify-content: center;
    letter-spacing: 0.3px;
  }
  .brand {
    position: absolute;
    top: 240px;
    left: 0;
    width: 800px;
    text-align: center;
    color: var(--plum-text);
    font-size: 70px;
    font-weight: 600;
    letter-spacing: 3px;
    line-height: 1;
  }
  .headline {
    position: absolute;
    top: 356px;
    left: 66px;
    color: var(--plum-text);
    font-size: 98px;
    font-weight: 400;
    letter-spacing: 1.5px;
    line-height: 1;
  }
  .contact {
    position: absolute;
    top: 460px;
    left: 73px;
    color: var(--plum-text);
    font-size: 27px;
    line-height: 38px;
    list-style: none;
  }
  .offer {
    position: absolute;
    left: 92px;
    top: 865px;
    width: 270px;
    height: 270px;
    border-radius: 50%;
    background: var(--pink);
    color: var(--white);
    text-align: center;
    display: flex;
    flex-direction: column;
    justify-content: center;
    align-items: center;
  }
  .offer__label { font-size: 22px; margin-bottom: 6px; }
  .offer__title {
    font-size: 40px;
    font-weight: 700;
    line-height: 38px;
  }
  .appointments {
    position: absolute;
    right: 42px;
    bottom: 22px;
    color: var(--white);
    font-size: 29px;
  }
</style>
</head>
<body>
<main class="ad">
  <div class="ad__sky"></div>
  <div class="ad__photo" role="img" aria-label="Foto: Silhouette einer Frau mit ausgebreiteten Armen auf einer Wiese vor violettem Abendhimmel"></div>

  <header class="topbar">Helga Brandner&nbsp;&nbsp;·&nbsp;&nbsp;Heilpraktikerin für Psychotherapie</header>

  <div class="brand">Lichtraum</div>

  <h1 class="headline">Praxiseröffnung</h1>

  <ul class="contact">
    <li>Lindenweg 14 / 72999 Talheim</li>
    <li>praxisraum.helgabrandner@mailpost.de</li>
    <li>01729385516 / www.praxisraum-brandner.org</li>
  </ul>

  <div class="offer">
    <div class="offer__label">aktuelles Angebot:</div>
    <div class="offer__title">Fantasiereise-<br>Entspannung<br>vom Alltags-<br>stress</div>
  </div>

  <p class="appointments">Termine nach Vereinbarung</p>
</main>
</body>
</html>
```